Willowmere Spa and Beauty Ltd. (Name of business)

I need a business card designed for this new company based out of Toronto Ontario. We specialize in Eyelash Extensions, Manicures and Pedicures, body waxing, massages, laser hair removal and botox treatments. Also offer a variety of products for sale, such as skin cream serums, collagen gel, eye cream, etc. It is a safe relaxing and non-judgemental environnment. Clients are welcome to come be pampered for the half or full day. Many service packages to choose from.

Open 7days per week from 8am to 8pm.

Priscilla Dunmore
Spa Facilitator
Willowmere Spa and Beauty Ltd.
7200 Harcourt St; Suite 1400
Toronto ON K2P 9W4

OFFICE: 416.790.4100
FAX: 416.790.4101
CELL: 416.632.1987
EMAIL: priscilla.dunmore@willowmerespa.com

Target Market(s)

Target market is primarily female ranging from 16 years old to 50 years old.

Industry/Entity Type

Business

Contact Information for Business Card

Priscilla Dunmore
Spa Facilitator
7200 Harcourt St; Suite 1400
Toronto ON K2P 9W4

OFFICE: 416.790.4100
FAX: 416.790.4101
CELL: 416.632.1987

Logo Text

I dont have a logo yet. I would like it simple but sophisticated and modern.

Font styles to use
Serif

Requirements
Must have
• all pertinent details such as company name, logo, name and contact information, services that are offered, including package rates
Nice to have
• Company name and logo prominent. A card that is neat and the information such as address, phone number, fax, email, etc is not too crowded but laid out in an easy to read format.
• Possibly on the back of card - some of the services offered could be listed, as well as professional cream lotions and serums. Hours of operation etc.

```html
<!DOCTYPE html>
<html lang="en">
<head>
<meta charset="utf-8">
<title>Willowmere Spa and Beauty Ltd. — Business Card</title>
<link rel="stylesheet" href="https://fonts.googleapis.com/css2?family=Lato:wght@300;400&display=swap">
<style>
  :root {
    --backdrop: #2a2a2c;
    --white: #ffffff;
    --pink: #e0429a;
    --pink-text: #d83c92;
    --pink-soft: #ec7fbf;
    --grey-text: #555058;
    --row-1: #b0519b;
    --row-2: #8e418b;
    --row-3: #71337a;
    --row-4: #552563;
    --plum-light: #b2479f;
    --plum-mid: #8a2f80;
    --plum-deep: #5e1b5d;
  }
  * { box-sizing: border-box; margin: 0; padding: 0; }
  html, body {
    width: 1200px; height: 1000px; overflow: hidden;
    background: var(--backdrop);
    font-family: "Lato", sans-serif;
  }
  .cards {
    position: relative; width: 1200px; height: 1000px;
    display: flex; justify-content: center; align-items: center; gap: 80px;
  }
  .card {
    position: relative; width: 360px; height: 630px; overflow: hidden;
    box-shadow: 0 14px 34px rgba(0,0,0,.45);
  }

  /* ---------- Front ---------- */
  .card-front { background: var(--white); }
  .front-accent {
    position: absolute; top: 38px; right: 18px; width: 44px; height: 3px;
    background: var(--pink-soft);
  }
  .hours {
    position: absolute; top: 48px; left: 0; width: 100%;
    text-align: center; color: var(--pink-soft);
    font-size: 15px; font-weight: 300; line-height: 1.35;
  }
  .brand-band {
    position: absolute; top: 102px; left: 0; width: 100%; height: 78px;
    background: var(--pink);
    display: flex; align-items: center; justify-content: center;
  }
  .brand-name {
    color: var(--white); font-size: 21px; font-weight: 300; letter-spacing: .5px;
  }
  .person {
    position: absolute; top: 228px; left: 28px;
    border-left: 7px solid var(--pink); padding-left: 16px;
  }
  .person-name { color: var(--pink-text); font-size: 30px; font-weight: 400; line-height: 1.1; }
  .person-title { color: var(--grey-text); font-size: 17px; font-weight: 300; margin-top: 4px; }

  .contact-list {
    position: absolute; top: 318px; left: 0; width: 100%; height: 312px;
    list-style: none; display: flex; flex-direction: column;
  }
  .contact-row {
    flex: 1; display: flex; align-items: center;
    color: var(--white); font-size: 15px; font-weight: 300; line-height: 1.4;
  }
  .contact-row:nth-child(1) { background: var(--row-1); }
  .contact-row:nth-child(2) { background: var(--row-2); }
  .contact-row:nth-child(3) { background: var(--row-3); }
  .contact-row:nth-child(4) { background: var(--row-4); }
  .contact-icon {
    width: 72px; height: 100%; flex: none;
    display: flex; align-items: center; justify-content: center;
    background: rgba(0,0,0,.1);
  }
  .contact-icon svg { width: 22px; height: 22px; fill: none; stroke: rgba(255,255,255,.8); stroke-width: 1.5; }
  .contact-text { padding-left: 22px; letter-spacing: .3px; }

  /* ---------- Back ---------- */
  .card-back {
    background: linear-gradient(160deg, var(--plum-light) 0%, var(--plum-mid) 55%, var(--plum-deep) 100%);
  }
  .back-facets {
    position: absolute; inset: 0;
    background: linear-gradient(200deg, rgba(255,255,255,.08) 0%, rgba(255,255,255,0) 45%, rgba(0,0,0,.12) 100%);
  }
  .back-brand {
    position: absolute; top: 200px; left: 0; width: 100%;
    text-align: center; color: var(--white);
    font-size: 30px; font-weight: 300; line-height: 1.35; letter-spacing: .5px;
  }
  .services {
    position: absolute; bottom: 44px; left: 0; width: 100%;
    text-align: center; color: rgba(255,255,255,.88);
    font-size: 12.5px; font-weight: 300; line-height: 1.6;
  }
</style>
</head>
<body>
<main class="cards">

  <section class="card card-front" aria-label="Business card front">
    <span class="front-accent"></span>
    <p class="hours">Open 7days per week<br>from 8am to 8pm</p>
    <div class="brand-band">
      <span class="brand-name">Willowmere Spa and Beauty Ltd</span>
    </div>
    <div class="person">
      <h1 class="person-name">Priscilla Dunmore</h1>
      <p class="person-title">Spa Facilitator</p>
    </div>
    <ul class="contact-list">
      <li class="contact-row">
        <span class="contact-icon">
          <svg viewBox="0 0 24 24"><path d="M6.5 3.5l3 3-1.8 2.2a12 12 0 0 0 7.6 7.6l2.2-1.8 3 3-2 2.5C11 19.5 4.5 13 4 5.5z"/></svg>
        </span>
        <span class="contact-text">416 632 1987<br>416 790 4100</span>
      </li>
      <li class="contact-row">
        <span class="contact-icon">
          <svg viewBox="0 0 24 24"><rect x="3" y="6" width="18" height="12"/><path d="M3 6l9 7 9-7"/></svg>
        </span>
        <span class="contact-text">priscilla.dunmore@willowmerespa.com</span>
      </li>
      <li class="contact-row">
        <span class="contact-icon">
          <svg viewBox="0 0 24 24"><rect x="7" y="3" width="10" height="6"/><rect x="3" y="9" width="18" height="8"/><rect x="7" y="14" width="10" height="7"/></svg>
        </span>
        <span class="contact-text">416 790 4101</span>
      </li>
      <li class="contact-row">
        <span class="contact-icon">
          <svg viewBox="0 0 24 24"><path d="M12 21s-6-6.5-6-11a6 6 0 0 1 12 0c0 4.5-6 11-6 11z"/><circle cx="12" cy="10" r="2.2"/></svg>
        </span>
        <span class="contact-text">7200 Harcourt St; Suite 1400<br>Toronto On K2P 9W4</span>
      </li>
    </ul>
  </section>

  <section class="card card-back" aria-label="Business card back">
    <div class="back-facets" role="img" aria-label="Faceted purple geometric background pattern"></div>
    <p class="back-brand">Willowmere Spa and<br>Beauty Ltd</p>
    <p class="services">
      Manicures and Pedicures | body waxing | laser hair<br>
      Removal and botox treatments | serums<br>
      Eyelash Extensions | massages
    </p>
  </section>

</main>
</body>
</html>
```